Moulding supply company needs a Door Hanger Design

Door Hanger Design Request from Ledge Craft
www. ledgecrafts.ca
We are moulding factory outlet in Toronto. Provide high quality moulding materials with competitive price like crown mouldings, casings, wainscoting, flatstocks, baseboards. We also provide professional installation for our clients. This door hanger will help the home owner easily find a local factory supplier with providing the materials as well as installation.

Detail request for design:
Size: 4”x11”, vertical
Shape: Rectangle

Content:
Front
1. Logo, see attachment(Use the left one, horizontal one)
2. Moulding factory outlet direct sale
3. Supply high quality Crown mouldings, baseboards, casings and wainscotings with competitive price
4. Installation & delivery
#2 content is the most important content, should be bold and readable
#3 can be smaller font compare to #2

Address: 47 West Falcon Ridge Rd, Maple Grove, MB R3K 2H8
Telephone: 204 555 0143
204 555 0178
Email: info@ledgecrafts.ca

Back
Slogan: Convert plain room into designer’s interiors

Telephone: 204 555 0143
204 555 0178
Email: info@ledgecrafts.ca

Images:
Front
1. Display our productions for crown mouldings, baseboards, casings and wainscotings, refer to our website www.ledgecrafts.ca. (The winner finally we will provide the high resolution images, low resolution please copy from our website so far)
Back
2. Display 4-6 nice images for 1. wainscoting walls 2. feature walls, 3. waffle ceiling like attached below. BUT PLEASE DON'T USE THE IMAGES PROVIDED, THIS IS ONLY A SAMPLE. Please use high resolution images for printing. ALSO PLEASE DON'T LIMIT YOUR CREATIVITY TO USE 4 SQUARES LIKE BELOW IMAGES. Please provide more ideas

Note:
1. Please do the bleeding for final printing production
2. Images have to be high resolution for ready to print
3. Style need to be fresh, clean, easy to read, modern and magazine style
4. Information has to be readable, easy to find, front and back both need to display company address, telephone, email, you can use icon or abbreviation to do these information.

Thanks,
Ledge Crafts

```html
<!DOCTYPE html>
<html lang="en">
<head>
<meta charset="utf-8">
<title>Ledge Crafts – Door Hangers</title>
<link href="https://fonts.googleapis.com/css2?family=Montserrat:wght@300;400;500;600;700&display=swap" rel="stylesheet">
<style>
  :root{
    --page:#756e6b;
    --hanger:#2b2a33;
    --hanger-deep:#1f1e25;
    --orange:#e4572e;
    --band:#efedea;
    --band-text:#85858c;
    --white:#ffffff;
    --rule:#4a4952;
    --icon-fill:#3b3a44;
  }
  *{box-sizing:border-box;margin:0;padding:0}
  html,body{width:1030px;height:1200px;overflow:hidden;background:var(--page)}
  body{position:relative;font-family:"Montserrat",Arial,sans-serif;color:var(--white)}

  .hanger{position:absolute;width:205px;height:556px;background:var(--hanger);
    border-radius:102.5px 102.5px 0 0;overflow:hidden}
  .hanger--front-a{left:290px;top:28px}
  .hanger--back-a{left:535px;top:28px}
  .hanger--front-b{left:290px;top:616px}
  .hanger--back-b{left:535px;top:616px}

  .photo{position:absolute;inset:0}
  .photo--lounge{background:
    linear-gradient(180deg,#2c2b33 0%,#33323a 30%,#3a3438 55%,#6d5350 78%,#3a3033 100%)}
  .photo--planter{background:
    linear-gradient(180deg,#2a2932 0%,#2f2e37 45%,#45463e 62%,#3a3940 78%,#2a292f 100%)}

  .hole{position:absolute;left:67px;top:53px;width:92px;height:92px;border-radius:50%;background:var(--page);z-index:3}
  .slit{position:absolute;left:0;top:99px;width:90px;height:8px;background:var(--page);z-index:3;
    clip-path:polygon(0 0,100% 10%,100% 90%,0 100%)}

  .front-title{position:absolute;left:23px;top:201px;font-size:15.5px;line-height:19px;font-weight:700;z-index:2}
  .front-body{position:absolute;left:23px;top:274px;font-size:9.4px;line-height:12px;font-weight:700;z-index:2}
  .front-note{position:absolute;left:23px;top:344px;font-size:9.4px;font-weight:700;z-index:2}

  .back-slogan{position:absolute;left:0;right:0;text-align:center;z-index:2;font-weight:700}
  .back-slogan .big{font-size:19px;line-height:22px}
  .back-slogan .mid{font-size:13px;line-height:17px;font-weight:600;margin-top:3px}
  .back-slogan .small{font-size:10px;line-height:14px;font-weight:600;margin-top:2px}
  .back-slogan--photo{top:226px}
  .back-slogan--list{top:170px;color:var(--orange)}

  .brand-edge{position:absolute;left:0;top:366px;width:205px;height:20px;background:var(--orange);
    clip-path:polygon(100% 0,100% 100%,0 100%,0 70%);z-index:2}
  .brand-band{position:absolute;left:0;top:376px;width:205px;height:82px;background:var(--band);
    clip-path:polygon(0 2%,100% 0,100% 100%,0 92%);z-index:2;display:flex;align-items:center;padding-left:22px;gap:7px}
  .brand-mark{width:13px;height:13px;background:var(--orange)}
  .brand-name{font-size:17px;font-weight:400;letter-spacing:1.5px;color:var(--band-text)}

  .contacts{position:absolute;left:22px;top:478px;z-index:2;font-size:6.2px;line-height:7.6px;font-weight:600}
  .contact-row{display:flex;gap:8px;margin-bottom:5px}
  .contact-row svg{width:7px;height:7px;flex:none;margin-top:1px}

  .catalogue{position:absolute;left:30px;width:143px;top:260px}
  .cat-label{font-size:6.4px;font-weight:700;letter-spacing:.2px}
  .cat-profiles{height:28px;margin:5px 0 7px;background:var(--icon-fill);border-radius:2px}
  .cat-profiles--short{width:58px}
  .cat-profiles--wide{width:136px}
  .cat-profiles--tall{height:32px}
  .cat-rule{height:1px;background:var(--rule);margin-bottom:7px}

  .web-band{position:absolute;left:0;bottom:0;width:205px;height:56px;background:var(--hanger-deep);text-align:center}
  .web-notch{position:absolute;left:95px;top:-1px;width:14px;height:8px;background:var(--hanger);
    clip-path:polygon(0 0,100% 0,50% 100%)}
  .web-lead{margin-top:20px;font-size:4.6px;font-weight:500;letter-spacing:.2px}
  .web-url{margin-top:5px;font-size:9.5px;font-weight:700;color:var(--orange);letter-spacing:.3px}
</style>
</head>
<body>

<section class="hanger hanger--front-a">
  <div class="photo photo--lounge" role="img" aria-label="Interior photo: dark panelled wall with faceted pendant lamp and blush armchair"></div>
  <div class="hole"></div><div class="slit"></div>
  <h1 class="front-title">MOULDING<br>FACTORY OUTLET<br>DIRECT SALE</h1>
  <p class="front-body">SUPPLY HIGH QUALITY<br>CROWN MOULDINGS,<br>BASEBOARDS, CASINGS<br>AND WAINSCOTINGS<br>WITH COMPETITIVE PRICE</p>
  <p class="front-note">INSTALLATION DELIVERY</p>
  <div class="brand-edge"></div>
  <div class="brand-band"><span class="brand-mark"></span><span class="brand-name">LEDGE CRAFTS</span></div>
  <div class="contacts">
    <div class="contact-row"><svg viewBox="0 0 10 10"><path d="M5 0a3.5 3.5 0 0 0-3.5 3.5C1.5 6 5 10 5 10s3.5-4 3.5-6.5A3.5 3.5 0 0 0 5 0zm0 5a1.4 1.4 0 1 1 0-2.8A1.4 1.4 0 0 1 5 5z" fill="#fff"/></svg><span>47 WEST FALCON RIDGE RD,<br>MAPLE GROVE, MB R3K 2H8</span></div>
    <div class="contact-row"><svg viewBox="0 0 10 10"><path d="M2 0l2 2.5-1 1.2a6 6 0 0 0 3.3 3.3l1.2-1L10 8l-1.2 1.6C4.5 10 0 5.5.4 1.2z" fill="#fff"/></svg><span>204 555 0143<br>204 555 0178</span></div>
    <div class="contact-row"><svg viewBox="0 0 10 10"><rect x="0" y="2" width="10" height="6.5" fill="#fff"/><path d="M0 2l5 3.5L10 2" stroke="#2b2a33" fill="none" stroke-width="1"/></svg><span>INFO@LEDGECRAFTS.CA</span></div>
  </div>
</section>

<section class="hanger hanger--back-a">
  <div class="photo photo--planter" role="img" aria-label="Interior photo: dark wainscoted wall with wire side table and potted grass planters"></div>
  <div class="hole"></div><div class="slit"></div>
  <div class="back-slogan back-slogan--photo">
    <div class="big">CONVERT</div>
    <div class="mid">PLAIN ROOM INTO</div>
    <div class="small">DESIGNER'S INTERIORS</div>
  </div>
  <div class="brand-edge"></div>
  <div class="brand-band"><span class="brand-mark"></span><span class="brand-name">LEDGE CRAFTS</span></div>
  <div class="contacts">
    <div class="contact-row"><svg viewBox="0 0 10 10"><path d="M5 0a3.5 3.5 0 0 0-3.5 3.5C1.5 6 5 10 5 10s3.5-4 3.5-6.5A3.5 3.5 0 0 0 5 0zm0 5a1.4 1.4 0 1 1 0-2.8A1.4 1.4 0 0 1 5 5z" fill="#fff"/></svg><span>47 WEST FALCON RIDGE RD,<br>MAPLE GROVE, MB R3K 2H8</span></div>
    <div class="contact-row"><svg viewBox="0 0 10 10"><path d="M2 0l2 2.5-1 1.2a6 6 0 0 0 3.3 3.3l1.2-1L10 8l-1.2 1.6C4.5 10 0 5.5.4 1.2z" fill="#fff"/></svg><span>204 555 0143<br>204 555 0178</span></div>
    <div class="contact-row"><svg viewBox="0 0 10 10"><rect x="0" y="2" width="10" height="6.5" fill="#fff"/><path d="M0 2l5 3.5L10 2" stroke="#2b2a33" fill="none" stroke-width="1"/></svg><span>INFO@LEDGECRAFTS.CA</span></div>
  </div>
</section>

<section class="hanger hanger--front-b">
  <div class="photo photo--lounge" role="img" aria-label="Interior photo: dark panelled wall with faceted pendant lamp and blush armchair"></div>
  <div class="hole"></div><div class="slit"></div>
  <h1 class="front-title">MOULDING<br>FACTORY OUTLET<br>DIRECT SALE</h1>
  <p class="front-body">SUPPLY HIGH QUALITY<br>CROWN MOULDINGS,<br>BASEBOARDS, CASINGS<br>AND WAINSCOTINGS<br>WITH COMPETITIVE PRICE</p>
  <p class="front-note">INSTALLATION DELIVERY</p>
  <div class="brand-edge"></div>
  <div class="brand-band"><span class="brand-mark"></span><span class="brand-name">LEDGE CRAFTS</span></div>
  <div class="contacts">
    <div class="contact-row"><svg viewBox="0 0 10 10"><path d="M5 0a3.5 3.5 0 0 0-3.5 3.5C1.5 6 5 10 5 10s3.5-4 3.5-6.5A3.5 3.5 0 0 0 5 0zm0 5a1.4 1.4 0 1 1 0-2.8A1.4 1.4 0 0 1 5 5z" fill="#fff"/></svg><span>47 WEST FALCON RIDGE RD,<br>MAPLE GROVE, MB R3K 2H8</span></div>
    <div class="contact-row"><svg viewBox="0 0 10 10"><path d="M2 0l2 2.5-1 1.2a6 6 0 0 0 3.3 3.3l1.2-1L10 8l-1.2 1.6C4.5 10 0 5.5.4 1.2z" fill="#fff"/></svg><span>204 555 0143<br>204 555 0178</span></div>
    <div class="contact-row"><svg viewBox="0 0 10 10"><rect x="0" y="2" width="10" height="6.5" fill="#fff"/><path d="M0 2l5 3.5L10 2" stroke="#2b2a33" fill="none" stroke-width="1"/></svg><span>INFO@LEDGECRAFTS.CA</span></div>
  </div>
</section>

<section class="hanger hanger--back-b">
  <div class="hole"></div><div class="slit"></div>
  <div class="back-slogan back-slogan--list">
    <div class="big">CONVERT</div>
    <div class="mid">PLAIN ROOM INTO</div>
    <div class="small">DESIGNER'S INTERIORS</div>
  </div>
  <div class="catalogue">
    <div class="cat-label">CROWN MOULDINGS</div>
    <div class="cat-profiles cat-profiles--short" role="img" aria-label="Line drawings of two crown moulding profiles"></div>
    <div class="cat-rule"></div>
    <div class="cat-label">WAINSCOTING</div>
    <div class="cat-profiles cat-profiles--wide" role="img" aria-label="Line drawings of four wainscoting profiles"></div>
    <div class="cat-rule"></div>
    <div class="cat-label">BASEBOARDS</div>
    <div class="cat-profiles cat-profiles--wide cat-profiles--tall" role="img" aria-label="Line drawings of five baseboard profiles"></div>
    <div class="cat-rule"></div>
    <div class="cat-label">CASINGS</div>
    <div class="cat-profiles cat-profiles--wide cat-profiles--tall" role="img" aria-label="Line drawings of six casing profiles"></div>
  </div>
  <div class="web-band">
    <div class="web-notch"></div>
    <p class="web-lead">TO LEARN MORE VISIT OUR WEBSITE</p>
    <p class="web-url">WWW.LEDGECRAFTS.CA</p>
  </div>
</section>

</body>
</html>
```